Lean Plate Daily Promo Postcard

Need 4x6 postcard created and similarly deisgned as attached postcard example. I have provided client notes:

Side A

(Left aligned image of fit cartoon chick - branded if possible)

“You'll love being Lean Plate Daily!" (company name in another color)

Text paragraph:

Lean Plate Daily is the most convenient, affordable, and flexible way to eat healthy, super nutritious, and squeaky clean food with a taste you’ll love!

Our meals are always freshly prepared, never frozen! We use the purest, local ingredients we can find, so forget about preservatives here and pesticides. All entrees are fitness focused and made to order. That means we can make your meals the way you want them, allowing us to accommodate:

-All Food Allergies
-Vegan Diets
-Paleo Diets
-Diets dictated by Personal Trainers & Doctors
-Or just plain picky eaters (you know who you are)

(Right aligned image bleed of healthy food dish)

Side B

(Upper left aligned Lean Plate Daily logo)

Reasons Why We Are Awesome:

- You get to choose your meals. We're here to help if you need us, but you won't get two of anything unless you ask for it!

-No contracts or hefty monthly fees. Seriously, no need to even cancel - you only pay for what you order. Sound good? Fist bump?

-We will be best friends! When you sign up with us, you get your own Lean Plate Daily advisor who will be by your side to help you make the right food choices and work with you to make us better for you. How cool is that!?

-We will pay you to promote us! You're not hallucinating. We pay more than ANY other healthy meal delivery company out there. Not only that but we pay it for as long as your friends stay our friends! Ask your advisor for details.

(Mid left aligned starburst call-to-action — “FREE Delivery For Life!”)

(Right aligned image of fit cartoon guy — branded if possible — message bubble — “Call us today to get started 833-415-2967”)

(Bottom centered web url no www - just = LeanPlateDaily.com)

```html
<!DOCTYPE html>
<html lang="en">
<head>
<meta charset="utf-8">
<title>Lean Plate Daily Promo Postcard</title>
<link rel="stylesheet" href="https://fonts.googleapis.com/css2?family=Kaushan+Script&family=Dancing+Script:wght@500&family=Zilla+Slab:wght@400;600&family=Nunito+Sans:wght@400;700;800&family=Open+Sans:ital,wght@1,700;1,800&family=Oswald:wght@600&display=swap">
<style>
  :root{
    --bg-light:#eef1ea;
    --bg-dark:#3d6416;
    --brand-green:#2aa84a;
    --leaf-green:#7ab648;
    --text-green:#2e7d3a;
    --sky-blue:#2e8fd0;
    --star-red:#d6262c;
    --ink:#222;
    --white:#ffffff;
  }
  *{margin:0;padding:0;box-sizing:border-box}
  html,body{width:1200px;height:1000px;overflow:hidden}
  body{
    position:relative;
    background:linear-gradient(100deg,var(--bg-light) 0%,#9fb487 35%,#5e8a33 70%,var(--bg-dark) 100%);
  }
  .card{position:absolute;left:293px;width:587px;overflow:hidden;background:var(--white)}
  .card--front{top:40px;height:456px}
  .card--back{top:502px;height:455px}

  .food-photo{
    position:absolute;inset:0;
    background:
      radial-gradient(ellipse 160px 60px at 60px 440px,#e0431f 0%,transparent 70%),
      radial-gradient(ellipse 140px 60px at 420px 450px,#f2c11a 0%,transparent 70%),
      radial-gradient(ellipse 200px 50px at 200px 10px,#8cc63e 0%,transparent 80%),
      radial-gradient(ellipse 120px 40px at 460px 20px,#c7302b 0%,transparent 70%),
      linear-gradient(180deg,#7fb83c 0%,#a8cf6a 20%,#d98a3a 60%,#c5412b 85%,#e8b53a 100%);
  }
  .front-panel{
    position:absolute;left:0;top:38px;width:587px;height:390px;
    background:rgba(255,255,255,0.82);
  }
  .runner-illustration{
    position:absolute;left:347px;top:15px;width:240px;height:441px;
    background:linear-gradient(180deg,#e0582a 0%,#f1b98a 30%,#6cbb3c 45%,#f3c9a0 60%,#5fb336 75%,#eebf95 100%);
    border-radius:120px 120px 30px 30px;
    opacity:.9;
  }
  .front-copy{position:absolute;left:40px;top:50px;width:320px}
  .tagline-lead{
    font-family:"Dancing Script",cursive;font-size:20px;color:#4f7f3a;margin-left:8px;
  }
  .tagline-name{
    font-family:"Kaushan Script",cursive;font-size:43px;color:var(--brand-green);
    line-height:1;margin-top:2px;white-space:nowrap;letter-spacing:-0.5px;
  }
  .tagline-swoosh{display:block;margin-top:-4px;margin-left:-10px}
  .front-body{
    font-family:"Zilla Slab",serif;font-size:12.6px;line-height:16px;color:var(--text-green);
    text-align:center;margin-top:14px;width:320px;margin-left:-4px;
  }
  .front-body p{margin-bottom:16px}
  .front-body ul{list-style:none}
  .brand-seal{
    position:absolute;left:462px;top:334px;width:116px;height:116px;border-radius:50%;
    background:var(--white);display:flex;align-items:center;justify-content:center;
    font-family:"Zilla Slab",serif;font-weight:600;font-size:15px;color:var(--brand-green);
    text-align:center;line-height:1.1;
  }

  .back-brand{
    position:absolute;left:120px;top:40px;display:flex;align-items:center;gap:8px;
    font-family:"Nunito Sans",sans-serif;font-weight:800;font-size:17px;color:var(--sky-blue);
  }
  .back-brand__dot{width:14px;height:14px;border-radius:50%;background:var(--leaf-green)}
  .reasons{position:absolute;left:32px;top:116px;width:262px}
  .reasons__title{
    font-family:"Nunito Sans",sans-serif;font-weight:800;font-size:16.5px;color:var(--leaf-green);
    letter-spacing:.2px;white-space:nowrap;
  }
  .reasons__list{list-style:none;margin-top:6px}
  .reasons__list li{
    font-family:"Nunito Sans",sans-serif;font-size:11.4px;line-height:14.6px;color:var(--text-green);
    margin-bottom:14.6px;
  }
  .reasons__list li.narrow{width:200px}
  .address-lines{position:absolute;left:321px;top:169px;width:227px}
  .address-lines span{display:block;height:19px;border-bottom:1.5px solid var(--sky-blue)}
  .starburst{position:absolute;left:230px;top:312px}
  .guy-illustration{
    position:absolute;left:447px;top:250px;width:140px;height:205px;
    background:linear-gradient(180deg,#6b4226 0%,#f2c39b 25%,#fbf3dc 50%,#e98b2c 70%,#5a86c0 100%);
    border-radius:70px 70px 10px 10px;opacity:.9;
  }
  .call-bubble{position:absolute;left:392px;top:248px}
  .site-url{
    position:absolute;left:335px;top:406px;
    font-family:"Open Sans",sans-serif;font-style:italic;font-weight:800;font-size:22px;
    color:var(--sky-blue);letter-spacing:-0.6px;
  }
</style>
</head>
<body>

<section class="card card--front">
  <div class="food-photo" role="img" aria-label="Full-bleed photograph of fresh vegetables and fruit"></div>
  <div class="front-panel"></div>
  <div class="runner-illustration" role="img" aria-label="Cartoon illustration of a fit red-haired woman jogging in green workout wear"></div>

  <div class="front-copy">
    <div class="tagline-lead">You'll love being,</div>
    <div class="tagline-name">Lean Plate Daily!</div>
    <svg class="tagline-swoosh" width="330" height="16" viewBox="0 0 330 16" aria-hidden="true">
      <path d="M2 12 C 90 4, 220 2, 328 6 C 220 6, 100 9, 2 14 Z" fill="var(--brand-green)"/>
    </svg>
    <div class="front-body">
      <p>Lean Plate Daily is the most convenient, affordable, and flexible way to eat healthy, super nutritious, and squeaky clean food with a taste you'll love!</p>
      <p>Our meals are always freshly prepared, never frozen! We use the purest, local ingredients we can find, so forget about preservatives here and pesticides. All entrees are fitness focused and made to order. That means we can make your meals the way you want them, allowing us to accommodate:</p>
      <ul>
        <li>All Food Allergies</li>
        <li>-Vegan Diets</li>
        <li>-Paleo Diets</li>
        <li>-Diets dictated by Personal Trainers &amp; Doctors</li>
        <li>-Or just plain picky eaters (you know who you are)</li>
      </ul>
    </div>
  </div>

  <div class="brand-seal">Lean Plate<br>Daily</div>
</section>

<section class="card card--back">
  <div class="back-brand"><span class="back-brand__dot"></span>Lean Plate Daily</div>

  <div class="reasons">
    <h2 class="reasons__title">REASON WHY WE ARE AWSOME</h2>
    <ul class="reasons__list">
      <li>- You get to choose your meals. We're here to help if you need us, but you won't get two of anything unless you ask for it!</li>
      <li>-No contracts or hefty monthly fees. Seriously, no need to even cancel - you only pay for what you order. Sound good? Fist bump?</li>
      <li>-We will be best friends! When you sign up with us, you get your own Lean Plate Daily advisor who will be by your side to help you make the right food choices and work with you to make us better for you. How cool is that!?</li>
      <li class="narrow">-We will pay you to promote us! You're not hallucinating. We pay more than ANY other healthy meal delivery company out there. Not only that but we pay it for as long as your friends stay our friends! Ask your advisor for details.</li>
    </ul>
  </div>

  <div class="address-lines"><span></span><span></span><span></span><span></span></div>

  <svg class="starburst" width="110" height="106" viewBox="0 0 110 106" aria-label="Free delivery for life">
    <polygon fill="var(--star-red)" points="55,2 64,16 80,8 82,25 100,24 94,40 108,50 94,60 102,76 85,78 82,96 66,88 55,104 44,88 28,96 25,78 8,76 16,60 2,50 16,40 10,24 28,25 30,8 46,16"/>
    <text x="55" y="42" text-anchor="middle" font-family="Oswald, sans-serif" font-weight="600" font-size="10.5" fill="#fff" font-style="italic">FREE DELIVERY</text>
    <text x="55" y="68" text-anchor="middle" font-family="Kaushan Script, cursive" font-size="24" fill="#1a1a1a">For Life!</text>
  </svg>

  <div class="guy-illustration" role="img" aria-label="Cartoon illustration of a fit young man lifting a dumbbell"></div>

  <svg class="call-bubble" width="112" height="66" viewBox="0 0 112 66" aria-label="Call us today to get started 833-415-2967">
    <path d="M6 30 C 6 10, 40 2, 58 2 C 80 2, 104 12, 104 30 C 104 46, 90 54, 70 56 L 108 62 L 80 52 C 70 56, 50 58, 40 56 C 20 54, 6 46, 6 30 Z" fill="var(--leaf-green)"/>
    <text x="14" y="24" font-family="Open Sans, sans-serif" font-style="italic" font-weight="800" font-size="10.5" fill="var(--ink)">Call us <tspan font-size="15">TODAY</tspan></text>
    <text x="26" y="36" font-family="Open Sans, sans-serif" font-style="italic" font-weight="700" font-size="9.5" fill="var(--ink)">to get started</text>
    <text x="12" y="50" font-family="Open Sans, sans-serif" font-style="italic" font-weight="800" font-size="12" fill="var(--ink)">833-415-2967</text>
  </svg>

  <div class="site-url">LeanPlateDaily.com</div>
</section>

</body>
</html>
```